Commercial/Retail/Office Real Estate Lease Brochure for Vacant Space

We need a commercial Real Estate Fyler Template for lease space. We would like it for Vacant lease spaces and new buildings in the commercial, retail, office and industrial lease space. The flyer should have sections for: Highlights (site size, leasable area, Location, Ammenties etc.), concept floor plan or site plan, contact information, project/construction description.

Target Market(s)

Commercial Leasing for Offices and Retail Space

Industry/Entity Type

Real Estate Leasing and Development

Requirements
Must have
• Clean, timeless not overly busy template with spots for key metrics (square feet leaseable space, parking etc), location for pictures
Nice to have
• Lorvex Crane Real Estate Logo for header/foot, reusable with adjustments for other spaces
Should not have
• Busy, overall colorfull or contrasting

```html
<!DOCTYPE html>
<html lang="en">
<head>
<meta charset="utf-8">
<title>Slate Point Centre – Retail Leasing Brochure</title>
<link rel="stylesheet" href="https://fonts.googleapis.com/css2?family=Montserrat:wght@600;700;800&family=Roboto:wght@400;500;700&display=swap">
<style>
:root{
  --backdrop:#e3e3e3;
  --paper:#ffffff;
  --rust:#c24f2c;
  --ink:#1b1b1b;
  --slate:#4a4d52;
  --mist:#ececec;
  --rule:#9a9a9a;
  --night:#1f1f1f;
}
*{margin:0;padding:0;box-sizing:border-box}
html,body{width:1200px;height:3000px;overflow:hidden}
body{background:var(--backdrop);font-family:"Roboto",Arial,sans-serif;color:var(--ink);position:relative}
.page{position:absolute;left:281px;width:638px;height:827px;background:var(--paper);overflow:hidden;box-shadow:6px 8px 10px rgba(0,0,0,.22)}
.page--cover{top:158px}
.page--features{top:1088px}
.page--snapshot{top:2015px}
.abs{position:absolute}

/* cover */
.hero{position:absolute;left:0;top:0}
.brand{position:absolute;left:50px;top:52px;display:flex;align-items:center;gap:12px;font-family:"Montserrat",sans-serif;font-weight:800;font-size:34px;color:var(--slate);letter-spacing:1px}
.brand__square{width:26px;height:26px;background:var(--rust)}
.partner{position:absolute;right:50px;top:44px;display:flex;align-items:center;gap:8px;font-weight:700;font-size:18px;color:var(--slate);background:rgba(255,255,255,.85);padding:12px 14px}
.partner__square{width:12px;height:12px;background:var(--slate)}
.cover-title{position:absolute;left:0;right:0;top:520px;text-align:center;font-family:"Montserrat",sans-serif;font-weight:800;font-size:54px;line-height:62px;letter-spacing:1px}
.cover-title .line1{color:var(--ink)}
.cover-title .accent{color:var(--rust)}
.cover-title .line2{color:var(--slate)}
.location-pill{position:absolute;left:85px;top:666px;width:465px;height:52px;border-radius:26px;background:var(--rust);color:#fff;display:flex;align-items:center;justify-content:center;gap:28px;font-family:"Montserrat",sans-serif;font-weight:700;font-size:22px}
.contact{position:absolute;top:756px;display:flex}
.contact__name{color:var(--rust);font-weight:700;font-size:15px;line-height:19px}
.contact__info{position:absolute;font-weight:700;font-size:11.5px;line-height:19px;white-space:nowrap}
.contacts__divider{position:absolute;left:305px;top:754px;width:1px;height:44px;background:var(--rule)}

/* features */
.section-title{position:absolute;left:46px;top:48px;font-size:29px;line-height:32px;color:#333;font-weight:400}
.section-title strong{display:block;color:var(--rust);font-weight:700}
.features-tab{position:absolute;left:0;top:129px;width:158px;height:28px;background:#dcdcdc;clip-path:polygon(0 0,92% 0,100% 50%,92% 100%,0 100%);font-weight:500;font-size:17px;line-height:28px;padding-left:47px;color:#222}
.feature-list{position:absolute;top:172px;list-style:none;font-size:11.6px;line-height:15px;color:#222}
.feature-list--left{left:48px;width:272px}
.feature-list--right{left:338px;width:262px}
.feature-list li{position:relative;padding-left:31px;margin-bottom:15px}
.feature-list li svg{position:absolute;left:0;top:1px}
.building-render{position:absolute;left:0;top:448px}

/* snapshot */
.snapshot-title{position:absolute;left:41px;top:48px;font-size:29px;color:#222;font-weight:400}
.snapshot-title strong{color:var(--rust);font-weight:700}
.fact-band{position:absolute;left:0;top:93px}
.fact{position:absolute;display:flex;gap:16px;font-size:12px;line-height:15px;color:#222}
.fact__text{width:210px}
.stat-label{position:absolute;font-size:12px;line-height:14px;color:#222}
.stat-value{position:absolute;font-weight:500;font-size:26px;color:var(--rust)}
.legend{position:absolute;left:187px;top:487px;list-style:none;font-size:10px;line-height:15.7px;color:#222}
.legend li{display:flex;align-items:center;gap:8px}
.legend i{display:inline-block;width:9px;height:9px}
.age-heading{position:absolute;left:334px;top:513px;font-size:12.5px;color:#222}
.age-row{position:absolute;left:334px;font-size:10px;color:#222;display:flex;align-items:center}
.age-row .dots{border-bottom:1px dotted #666;margin:0 4px 0 6px;height:8px}
.age-row b{color:var(--rust);font-size:12px}
.income{position:absolute;left:334px;font-size:12.5px;color:#222}
.income b{color:var(--rust);font-size:15px;margin-left:14px}
.footer{position:absolute;left:0;top:707px;width:638px;height:120px;background:var(--night);color:#fff}
.footer__person{position:absolute;left:43px;display:flex;gap:45px}
.footer__name{color:var(--rust);font-weight:700;font-size:14px;line-height:17px;width:65px}
.footer__info{font-weight:700;font-size:10.5px;line-height:17px;white-space:nowrap}
.footer__divider{position:absolute;left:318px;top:24px;width:1px;height:72px;background:#777}
.footer__inquiries{position:absolute;left:366px;top:32px;font-weight:700;font-size:14px}
.footer__tagline{position:absolute;left:366px;top:58px;font-weight:700;font-size:15.5px;line-height:20px}
.footer__brand{position:absolute;left:514px;top:38px;display:flex;align-items:center;gap:7px;background:#fff;color:var(--slate);font-weight:700;font-size:13px;padding:10px 9px}
.footer__brand i{width:9px;height:9px;background:var(--slate)}
</style>
</head>
<body>

<section class="page page--cover">
  <svg class="hero" width="638" height="485" viewBox="0 0 638 485" role="img" aria-label="Architectural rendering of a brick and stone two-storey retail building with parking, shoppers and flower beds under a blue sky">
    <defs>
      <linearGradient id="heroSky" x1="0" y1="0" x2="0" y2="1">
        <stop offset="0" stop-color="#8fb6df"/>
        <stop offset=".55" stop-color="#c6d8ea"/>
        <stop offset=".75" stop-color="#7a5a4c"/>
        <stop offset="1" stop-color="#6f8a4f"/>
      </linearGradient>
    </defs>
    <path d="M0 0H638V380Q480 490 330 485Q150 480 0 360Z" fill="url(#heroSky)"/>
  </svg>
  <div class="brand"><span class="brand__square"></span>SLATE POINT</div>
  <div class="partner"><span class="partner__square"></span>Halvard Realty</div>

  <h1 class="cover-title"><span class="line1">RETAIL </span><span class="accent">LEASING</span><br><span class="line2">OPPORTUNITY</span></h1>

  <div class="location-pill">
    <svg width="16" height="22" viewBox="0 0 16 22" aria-hidden="true"><path d="M8 0C3.6 0 0 3.5 0 7.9 0 13.5 8 22 8 22s8-8.5 8-14.1C16 3.5 12.4 0 8 0z" fill="#fff"/><circle cx="8" cy="8" r="3" fill="#c24f2c"/></svg>
    <span>Moncton,New Brunswick</span>
  </div>

  <div class="contact" style="left:46px">
    <div class="contact__name">RENÉE<br>ARSENAULT</div>
  </div>
  <div class="contact__info" style="left:135px;top:756px">(506) 555-0141<br>r.arsenault@halvard.ca</div>
  <div class="contacts__divider"></div>
  <div class="contact" style="left:328px">
    <div class="contact__name">COLETTE<br>BRISSON</div>
  </div>
  <div class="contact__info" style="left:424px;top:756px">(506) 555-0187<br>c.brisson@halvard.ca</div>
</section>

<section class="page page--features">
  <h2 class="section-title">Prime Commercial Space<strong>For Lease</strong></h2>
  <div class="features-tab">Features</div>

  <ul class="feature-list feature-list--left">
    <li><svg width="14" height="14" viewBox="0 0 14 14"><circle cx="7" cy="7" r="6" fill="none" stroke="#333"/><path d="M4 7.2l2 2 4-4" fill="none" stroke="#333"/></svg>Anchored by Bulkmart Wholesale &amp; Gas Bar.</li>
    <li><svg width="14" height="14" viewBox="0 0 14 14"><circle cx="7" cy="7" r="6" fill="none" stroke="#333"/><path d="M4 7.2l2 2 4-4" fill="none" stroke="#333"/></svg>Current site tenants include Burger Harbour, Bean Coast Coffee, Maplerow Design Studio, and The Kibble &amp; Crate Co.</li>
    <li><svg width="14" height="14" viewBox="0 0 14 14"><circle cx="7" cy="7" r="6" fill="none" stroke="#333"/><path d="M4 7.2l2 2 4-4" fill="none" stroke="#333"/></svg>Close proximity to Elmwood commercial node.</li>
    <li><svg width="14" height="14" viewBox="0 0 14 14"><circle cx="7" cy="7" r="6" fill="none" stroke="#333"/><path d="M4 7.2l2 2 4-4" fill="none" stroke="#333"/></svg>Offers fantastic visibility from the Trans-Canada Highway.</li>
    <li><svg width="14" height="14" viewBox="0 0 14 14"><circle cx="7" cy="7" r="6" fill="none" stroke="#333"/><path d="M4 7.2l2 2 4-4" fill="none" stroke="#333"/></svg>High traffic area with average daily vehicle counts of:</li>
    <li><svg width="14" height="14" viewBox="0 0 14 14"><circle cx="7" cy="7" r="6" fill="none" stroke="#333"/><path d="M4 7.2l2 2 4-4" fill="none" stroke="#333"/></svg>±25,000 vehicles daily at the intersection of Slate Drive and Elmwood</li>
  </ul>
  <ul class="feature-list feature-list--right">
    <li><svg width="14" height="14" viewBox="0 0 14 14"><circle cx="7" cy="7" r="6" fill="none" stroke="#333"/><path d="M4 7.2l2 2 4-4" fill="none" stroke="#333"/></svg>Drive (43% increase since Bulkmart Wholesale has opened)</li>
    <li><svg width="14" height="14" viewBox="0 0 14 14"><circle cx="7" cy="7" r="6" fill="none" stroke="#333"/><path d="M4 7.2l2 2 4-4" fill="none" stroke="#333"/></svg>±23,300 vehicles daily on the Trans Canada Highway</li>
    <li><svg width="14" height="14" viewBox="0 0 14 14"><circle cx="7" cy="7" r="6" fill="none" stroke="#333"/><path d="M4 7.2l2 2 4-4" fill="none" stroke="#333"/></svg>From 1,315 - 48,200 SF available for lease.</li>
    <li><svg width="14" height="14" viewBox="0 0 14 14"><circle cx="7" cy="7" r="6" fill="none" stroke="#333"/><path d="M4 7.2l2 2 4-4" fill="none" stroke="#333"/></svg>3 points of access to Slate Point Centre from the Trans-Canada Highway</li>
    <li><svg width="14" height="14" viewBox="0 0 14 14"><circle cx="7" cy="7" r="6" fill="none" stroke="#333"/><path d="M4 7.2l2 2 4-4" fill="none" stroke="#333"/></svg>Minutes from Caledonia Industrial Park which has over 6,000,000 SF / 145 Businesses / 3,700 employees</li>
  </ul>

  <svg class="building-render" width="638" height="379" viewBox="0 0 638 379" role="img" aria-label="Architectural rendering of a two-storey brick and dark-panel office building with landscaping and a parked car at dusk">
    <defs>
      <linearGradient id="renderSky" x1="0" y1="0" x2="0" y2="1">
        <stop offset="0" stop-color="#5d7a96"/>
        <stop offset=".5" stop-color="#b8c7d2"/>
        <stop offset=".7" stop-color="#7d5f50"/>
        <stop offset="1" stop-color="#3e4a44"/>
      </linearGradient>
    </defs>
    <path d="M0 0Q320 120 638 0V379H0Z" fill="url(#renderSky)"/>
  </svg>
</section>

<section class="page page--snapshot">
  <h2 class="snapshot-title">Moncton <strong>SNAPSHOT</strong></h2>
  <svg class="fact-band" width="638" height="256" viewBox="0 0 638 256" aria-hidden="true">
    <path d="M0 0H638V256H0Z" fill="#ececec"/>
    <path d="M0 0H638Q320 45 0 0Z" fill="#fff"/>
  </svg>

  <div class="fact" style="left:58px;top:143px">
    <svg width="30" height="30" viewBox="0 0 30 30"><rect x="2" y="3" width="26" height="19" rx="5" fill="#c24f2c"/><path d="M8 21l-2 7 8-6z" fill="#c24f2c"/><rect x="9" y="10" width="12" height="2" fill="#fff"/></svg>
    <div class="fact__text">Moncton boasts a 47% bilingual workforce and is Canada's first bilingual city.</div>
  </div>
  <div class="fact" style="left:54px;top:197px">
    <svg width="36" height="30" viewBox="0 0 36 30"><rect x="2" y="8" width="32" height="16" fill="none" stroke="#c24f2c" stroke-width="2.5"/><circle cx="18" cy="16" r="4" fill="#c24f2c"/></svg>
    <div class="fact__text">On average, New Brunswick cities have an 18% business cost advantage over the G7 average (Brightline Advisory Competitive Alternatives 2016)</div>
  </div>
  <div class="fact" style="left:54px;top:275px">
    <svg width="36" height="34" viewBox="0 0 36 34"><rect x="4" y="22" width="5" height="10" fill="#c24f2c"/><rect x="12" y="18" width="5" height="14" fill="#c24f2c"/><rect x="20" y="14" width="5" height="18" fill="#c24f2c"/><path d="M3 16L14 8l6 4 12-9" fill="none" stroke="#c24f2c" stroke-width="2.5"/></svg>
    <div class="fact__text" style="width:200px">Tourism and retail employ 23.5% of the total workforce in Moncton. That just gives you a sense of what a bustling retail hub Moncton really is.</div>
  </div>
  <div class="fact" style="left:336px;top:143px">
    <svg width="34" height="34" viewBox="0 0 34 34"><rect x="4" y="12" width="10" height="20" fill="#c24f2c"/><rect x="14" y="2" width="16" height="30" fill="#c24f2c"/><rect x="18" y="7" width="3" height="3" fill="#fff"/><rect x="24" y="7" width="3" height="3" fill="#fff"/><rect x="18" y="14" width="3" height="3" fill="#fff"/><rect x="24" y="14" width="3" height="3" fill="#fff"/></svg>
    <div class="fact__text" style="width:200px">Moncton is the #1 Commercial &amp; Industrial Hub in Atlantic Canada according to Statistics Canada.</div>
  </div>
  <div class="fact" style="left:332px;top:198px">
    <svg width="40" height="30" viewBox="0 0 40 30"><path d="M2 12l9-7 9 6 9-6 9 7-10 11c-3 3-13 3-16 0z" fill="#c24f2c"/></svg>
    <div class="fact__text" style="width:212px">Moncton named one of the best places in Canada to do business for 5 consecutive years by Northern Commerce</div>
  </div>
  <div class="fact" style="left:332px;top:275px">
    <svg width="40" height="30" viewBox="0 0 40 30"><path d="M20 3L38 11 20 19 2 11z" fill="#c24f2c"/><path d="M10 15v8c5 4 15 4 20 0v-8l-10 5z" fill="#c24f2c"/></svg>
    <div class="fact__text" style="width:212px">Over 13,500 students enrolled in postsecondary education programs in the Greater Moncton region.</div>
  </div>

  <div class="stat-label" style="left:44px;top:371px">Current population<br>Estimates</div>
  <div class="stat-value" style="left:189px;top:364px">155,825</div>
  <div class="stat-label" style="left:44px;top:418px">Population within<br>2.5 hour drive</div>
  <div class="stat-value" style="left:175px;top:410px">1,400,000</div>
  <div class="stat-label" style="left:334px;top:371px">Economic region<br>Population</div>
  <div class="stat-value" style="left:469px;top:364px">220,000</div>
  <div class="stat-label" style="left:334px;top:418px;width:160px">Best retail shopping environment In atlantic canada with impressive Average annual retail sales of</div>
  <div class="stat-value" style="left:508px;top:408px;line-height:30px">2,6,<br>BILLION</div>

  <div class="stat-label" style="left:44px;top:487px">Retail sales<br>By major city<br>Moncton cma - 2011</div>
  <ul class="legend">
    <li><i style="background:#c24f2c"></i>Vehicles &amp; Related</li>
    <li><i style="background:#5b6770"></i>Gas Stations</li>
    <li><i style="background:#2f3d47"></i>Supermarkets / Food</li>
    <li><i style="background:#c8b52e"></i>Merchandise / Stores</li>
    <li><i style="background:#5ecfc4"></i>Home-related</li>
    <li><i style="background:#9cb52f"></i>Clothing / Jewelery</li>
    <li><i style="background:#1e2a5a"></i>Pharmacy</li>
    <li><i style="background:#f3a7b8"></i>Others</li>
  </ul>
  <svg class="abs" style="left:40px;top:538px" width="230" height="165" viewBox="0 0 230 165" role="img" aria-label="Bar chart of retail sales by category">
    <g font-family="Roboto, sans-serif" font-size="10" fill="#222" text-anchor="end">
      <text x="14" y="12">25</text><text x="14" y="42">20</text><text x="14" y="72">15</text><text x="14" y="101">10</text><text x="14" y="131">5</text>
    </g>
    <path d="M21 4V158" stroke="#333"/>
    <g stroke="#333"><path d="M18 9H21M18 39H21M18 68H21M18 98H21M18 128H21"/></g>
    <rect x="25" y="18" width="22" height="140" fill="#c24f2c"/>
    <rect x="49" y="27" width="22" height="131" fill="#5b6770"/>
    <rect x="73" y="49" width="22" height="109" fill="#2f3d47"/>
    <rect x="97" y="97" width="22" height="61" fill="#c8b52e"/>
    <rect x="121" y="97" width="22" height="61" fill="#5ecfc4"/>
    <rect x="145" y="117" width="22" height="41" fill="#9cb52f"/>
    <rect x="169" y="108" width="22" height="50" fill="#1e2a5a"/>
    <rect x="193" y="127" width="22" height="31" fill="#f3a7b8"/>
  </svg>

  <div class="age-heading">MEDIAN POPULATION AGE (IN YEARS)</div>
  <div class="age-row" style="top:548px">Greater Moncton<span class="dots" style="width:92px"></span><b>42.1</b></div>
  <div class="age-row" style="top:566px">New Brunswick<span class="dots" style="width:100px"></span><b>45.7</b></div>
  <div class="age-row" style="top:584px">Canada<span class="dots" style="width:132px"></span><b>44.2</b></div>
  <div class="income" style="top:612px">MEDIAN FAMILY INCOME <b>$72,240</b></div>
  <div class="income" style="top:639px">AVERAGE FAMILY INCOME <b>$73,073</b></div>

  <footer class="footer">
    <div class="footer__person" style="top:28px">
      <div class="footer__name">RENÉE<br>ARSENAULT</div>
      <div class="footer__info">(506) 555-0141<br>r.arsenault@halvard.ca</div>
    </div>
    <div class="footer__person" style="top:72px">
      <div class="footer__name">COLETTE<br>BRISSON</div>
      <div class="footer__info">(506) 555-0187<br>c.brisson@halvard.ca</div>
    </div>
    <div class="footer__divider"></div>
    <div class="footer__inquiries">LEASING INQUIRIES</div>
    <div class="footer__tagline">Spaces<br>That Work</div>
    <div class="footer__brand"><i></i>Halvard Realty</div>
  </footer>
</section>

</body>
</html>
```